Stationary Design Letterhead and Envelope

Artist should provide Letterhead and envelop stationary designs

Info for stationary:
Fenwarde Outdoor Advertising
4857 Mesa Rd. 318 N. PO BOX 582917
Austin, TX 78651

Dale Fenwarde
President
512-608-2917
dale@fenwardeoutdoor.example
fenwardeoutdoor.example

Target Market(s)

clients

Colors
0054AA
0677BA
7BADD7
CADEEF
E8F1F8

Requirements
Must have
• high quality unique eye catching and dynamic

```html
<!DOCTYPE html>
<html lang="en">
<head>
<meta charset="utf-8">
<title>Fenwarde Outdoor Advertising – Letterhead</title>
<link rel="stylesheet" href="https://fonts.googleapis.com/css2?family=Montserrat:wght@500;700&family=Alex+Brush&display=swap">
<style>
  :root {
    --backdrop: #eceff0;
    --paper: #ffffff;
    --ink: #111111;
    --brand-blue: #1e7be6;
  }
  * { margin: 0; padding: 0; box-sizing: border-box; }
  html, body {
    width: 1058px; height: 1200px; overflow: hidden;
    background: var(--backdrop);
    font-family: "Montserrat", Arial, sans-serif;
    color: var(--ink);
  }
  .letterhead {
    position: absolute; left: 90px; top: 35px;
    width: 878px; height: 1130px;
    background: var(--paper);
    overflow: hidden;
  }
  .brand {
    position: absolute; left: 58px; top: 100px;
    display: flex; align-items: center; gap: 10px;
  }
  .brand-mark { width: 26px; height: 26px; background: var(--brand-blue); }
  .brand-name {
    font-weight: 700; font-size: 20px; letter-spacing: 1px;
    color: var(--brand-blue); line-height: 1.2;
  }
  .contact {
    position: absolute; left: 552px; top: 66px;
    list-style: none;
    font-size: 14px; font-weight: 500; letter-spacing: 1.6px;
  }
  .contact li {
    display: flex; align-items: flex-start; gap: 14px;
    height: 30px; line-height: 17px;
  }
  .contact svg { width: 16px; height: 16px; flex: none; margin-top: 1px; }
  .recipient {
    position: absolute; left: 58px; top: 262px;
    font-weight: 700; font-size: 15px; letter-spacing: 1.6px; line-height: 19.5px;
  }
  .body-copy {
    position: absolute; left: 58px; top: 380px; width: 764px;
    font-size: 19px; font-weight: 500; letter-spacing: 2.1px; line-height: 30.7px;
  }
  .body-copy p { margin-bottom: 30.7px; }
  .body-copy .line { display: block; text-align: justify; text-align-last: justify; white-space: nowrap; }
  .body-copy .line.last { text-align-last: left; }
  .signature {
    position: absolute; left: 56px; top: 840px;
    font-family: "Alex Brush", cursive; font-size: 38px; line-height: 1;
  }
  .signer-title {
    position: absolute; left: 56px; top: 890px;
    font-size: 25px; font-weight: 500; letter-spacing: 2px;
  }
  .footer-band {
    position: absolute; left: 0; bottom: 0; width: 100%; height: 37px;
    background: var(--brand-blue);
  }
</style>
</head>
<body>
<main class="letterhead">
  <header>
    <div class="brand">
      <span class="brand-mark"></span>
      <div class="brand-name">FENWARDE<br>OUTDOOR ADVERTISING</div>
    </div>
    <ul class="contact">
      <li>
        <svg viewBox="0 0 16 16" fill="none" stroke="#222" stroke-width="1.1"><path d="M4 1.5l2.2 3-1.4 1.6c.8 2 2.2 3.4 4.1 4.2l1.6-1.4 3 2.2-1.3 2.2c-5.6-.6-9.6-4.6-10.2-10.2z"/><path d="M9.5 2.5a4 4 0 0 1 4 4M9.5 .8a5.7 5.7 0 0 1 5.7 5.7"/></svg>
        <span>512-608-2917</span>
      </li>
      <li>
        <svg viewBox="0 0 16 16" fill="none" stroke="#222" stroke-width="1.1"><rect x="1" y="3.5" width="14" height="9"/><path d="M1 3.5l7 5.5 7-5.5M1 12.5l5-4.5M15 12.5l-5-4.5"/></svg>
        <span>dale@fenwardeoutdoor.example</span>
      </li>
      <li>
        <svg viewBox="0 0 16 16" fill="none" stroke="#222" stroke-width="1.1"><circle cx="8" cy="8" r="6.8"/><ellipse cx="8" cy="8" rx="3" ry="6.8"/><path d="M1.2 8h13.6M2.2 4.5h11.6M2.2 11.5h11.6"/></svg>
        <span>fenwardeoutdoor.example</span>
      </li>
      <li>
        <svg viewBox="0 0 16 16" fill="none" stroke="#222" stroke-width="1.1"><path d="M8 12.5S4.5 8.8 4.5 6a3.5 3.5 0 0 1 7 0c0 2.8-3.5 6.5-3.5 6.5z"/><circle cx="8" cy="6" r="1.3"/><ellipse cx="8" cy="13.5" rx="5.5" ry="1.6"/></svg>
        <span>4857 Mesa Rd. 318 N.<br>Austin, TX 78651</span>
      </li>
    </ul>
  </header>

  <address class="recipient" style="font-style:normal">
    TO<br>Rafiq Haldern<br>Brennmoor, Valdoria
  </address>

  <section class="body-copy">
    <p>
      <span class="line">Lorem ipsum dolor sit amet, consectetur adipisicing elit, sed</span>
      <span class="line">do eiusmod tempor incididunt ut labore et dolore magna</span>
      <span class="line">aliqua. Ut enim ad minim veniam, quis nostrud exercitation ul-</span>
      <span class="line last">lamco laboris nis</span>
    </p>
    <p>
      <span class="line">aliquip ex ea commodo consequat. Duis aute irure dolor in rep-</span>
      <span class="line">rehenderit in voluptate velit esse cillum dolore eu fugiat nulla</span>
      <span class="line last">pariatur. Excepteur sint occaecat</span>
    </p>
    <p>
      <span class="line">perspiciatis unde omnis iste natus error sit voluptatem accu-</span>
      <span class="line">santium doloremque laudantium, totam rem aperiam, eaque</span>
      <span class="line">ipsa quae ab illo inventore veritatis et quasi architecto beatae</span>
      <span class="line last">vitae dicta sunt explicabo. Nemo enim</span>
    </p>
  </section>

  <div class="signature">Dale Fenwarde</div>
  <div class="signer-title">President</div>

  <div class="footer-band"></div>
</main>
</body>
</html>
```